Business Card Design Project

Corvexa logo will be provided after
Front

Bram Oskarsen- Construction Manager

Ph: (61) 07 53182907
boskarsen@corvexa.com.au
PO Box 83 Kelbarra 4529

Back
Corvexa
EPCM

Oil - Gas - Mining

Industry/Entity Type

Business

Font styles to use
Sans Serif

Colors
faa54b

Requirements
Must have
• White Back Ground

```html
<!DOCTYPE html>
<html lang="en">
<head>
<meta charset="utf-8">
<title>Corvexa Business Card</title>
<link rel="stylesheet" href="https://fonts.googleapis.com/css2?family=Source+Sans+3:wght@400;600;700;900&display=swap">
<style>
  :root {
    --bg: #2a1c17;
    --orange: #f68d22;
    --black: #050505;
    --white: #ffffff;
    --ink: #2b2b2b;
  }
  * { margin: 0; padding: 0; box-sizing: border-box; }
  html, body { width: 1136px; height: 1200px; overflow: hidden; }
  body {
    background: var(--bg);
    font-family: "Source Sans 3", sans-serif;
    position: relative;
  }
  .card {
    position: absolute;
    border-radius: 20px;
    overflow: hidden;
  }
  .card--front {
    left: 192px; top: 88px; width: 848px; height: 484px;
    background: var(--white);
  }
  .card--back {
    left: 97px; top: 629px; width: 847px; height: 483px;
    background: var(--orange);
  }
  .front-header {
    position: absolute; inset: 0; width: 100%; height: 100%;
  }
  .holder {
    position: absolute; right: 25px; top: 26px; text-align: right; color: var(--white);
  }
  .holder__name { font-size: 29px; font-weight: 700; line-height: 1.15; }
  .holder__role { font-size: 21px; font-weight: 400; line-height: 1.3; }
  .wordmark {
    position: absolute;
    display: flex; align-items: center; gap: 18px;
    font-weight: 900; font-size: 80px; letter-spacing: 8px; line-height: 1;
    white-space: nowrap;
  }
  .wordmark__dot {
    width: 34px; height: 34px; border-radius: 50%;
  }
  .card--front .wordmark { left: 43px; top: 178px; color: var(--black); }
  .card--front .wordmark__dot { background: var(--orange); }
  .card--back .wordmark { left: 157px; top: 178px; color: var(--black); }
  .card--back .wordmark__dot { background: var(--white); }
  .contacts {
    position: absolute; left: 55px; top: 360px; list-style: none;
    color: var(--ink); font-size: 22px;
  }
  .contacts li { display: flex; align-items: center; gap: 10px; height: 28px; white-space: nowrap; }
  .contacts svg { width: 19px; height: 19px; flex: none; }
  .divider {
    position: absolute; left: 362px; top: 418px; width: 1px; height: 28px; background: #c8c8c8;
  }
  .address {
    position: absolute; left: 387px; top: 422px; color: var(--ink); font-size: 22px; white-space: nowrap;
  }
  .back-tagline {
    position: absolute; left: 157px; top: 306px;
    color: var(--white); font-size: 25px; letter-spacing: 4.5px; white-space: nowrap;
  }
  .back-tagline__lead { font-weight: 700; }
</style>
</head>
<body>
  <section class="card card--front">
    <svg class="front-header" viewBox="0 0 895 511" preserveAspectRatio="none" aria-hidden="true">
      <defs>
        <linearGradient id="swoosh" x1="0" x2="1" y1="0" y2="0">
          <stop offset="0" stop-color="#222"/>
          <stop offset="0.6" stop-color="#555"/>
          <stop offset="1" stop-color="#bbb" stop-opacity="0"/>
        </linearGradient>
      </defs>
      <path d="M0 0 H895 V212 C560 50 250 40 0 92 Z" fill="var(--black)"/>
      <path d="M0 92 C250 40 560 50 895 212 L895 262 C600 95 300 72 0 108 Z" fill="var(--orange)"/>
      <path d="M0 110 C140 75 320 62 460 88 C320 78 150 92 0 138 Z" fill="url(#swoosh)"/>
    </svg>
    <div class="holder">
      <div class="holder__name">Bram Oskarsen</div>
      <div class="holder__role">Construction Manager</div>
    </div>
    <div class="wordmark"><span>CORVEXA</span><span class="wordmark__dot"></span></div>
    <ul class="contacts">
      <li>
        <svg viewBox="0 0 20 20"><circle cx="10" cy="10" r="8.5" fill="none" stroke="var(--orange)" stroke-width="1.5"/><path d="M7 5.5 L9 8 L8 9.5 C8.8 11 9.6 11.8 10.8 12.4 L12.2 11.3 L14.5 13.2 L13.3 14.6 C10 14.5 6 10.5 5.8 7 Z" fill="var(--orange)"/></svg>
        (61) 07 53182907
      </li>
      <li>
        <svg viewBox="0 0 20 20"><path d="M2 8 L10 3 L18 8 V16 H2 Z" fill="var(--orange)"/><path d="M2 8 L10 13 L18 8" fill="none" stroke="#fff" stroke-width="1.3"/></svg>
        boskarsen@corvexa.com.au
      </li>
      <li>
        <svg viewBox="0 0 20 20"><circle cx="10" cy="10" r="8.5" fill="none" stroke="var(--orange)" stroke-width="1.4"/><ellipse cx="10" cy="10" rx="3.8" ry="8.5" fill="none" stroke="var(--orange)" stroke-width="1.2"/><path d="M1.5 10 H18.5 M3 6 H17 M3 14 H17" stroke="var(--orange)" stroke-width="1.1"/></svg>
        www.corvexa.com.au
      </li>
    </ul>
    <div class="divider"></div>
    <div class="address">PO Box 83 Kelbarra 4529</div>
  </section>

  <section class="card card--back">
    <div class="wordmark"><span>CORVEXA</span><span class="wordmark__dot"></span></div>
    <div class="back-tagline"><span class="back-tagline__lead">EPCM</span> · Oil - Gas - Mining</div>
  </section>
</body>
</html>
```